Law Enforcement Consulting Group Website

We are working with a Law Enforcement Consulting Group called Brennock Group. They help law enforcement agencies develop policies, training tools, solve problems, etc...

Some sites to use for content/competitors:
https://harrowfieldpartners.com
https://veltranorix.com/military-law/law-enforcement-consulting-services/
https://harrowfieldpartners.com/services/police-services/

Consulting websites for inspiration ( we found these sites to fit better with the brand, and identity of the client:

https://drum.quelby
https://tidalvoxen.co
https://www.torvendabrill.com
https://quellaromberti.com
https://perisovandeh.com
https://themes.pebblecrate.com/be/consultant2/
https://themes.pebblecrate.com/be/consultant/

Thank you for taking the time to consider designing a website for us. We are web developers based in Stockton, CA, USA. Most of our projects go through the same process. Understanding this process may help you win a project with us. We custom-code all of our websites in-house. We don’t have any requirements as to what tools you use for your design, but we prefer Figma files. For any design that we label as four-stars, we send it to the client for review. The client picks the final design they want us to use. Once we complete this process, we will continue to show additional clients all the four-star sites and purchase them later. Your designs will have multiple chances to sell. For better chances of success, we ask that you follow these guidelines.

IMAGES:
If you use any images or icons in the design, we ask that you have a link to the asset so we can purchase the image/icon. Most of the designs we submit do not have the customer’s images on them unless they have some great images. Be creative; show us the feeling you are trying to portray with your image choices. Use any royalty-free site you choose. We subscribe to Adobe and mainly use their images, but we can purchase images outside of Adobe.
PLEASE NOTE: we will not submit designs to clients with watermarks on the images.

FONTS:
We ask that you identify the fonts used in the design. This can be done in a message if you want. We typically use Google Fonts and Adobe Fonts.

CONTENT:
We're always open to different content and ideas. We often submit designs with stock images so the client can see our vision. We typically take pictures after the website launch to use their images with our vision. Lorem Ipsum is fine for paragraphs, but we ask that you write the headers in correct English. We want to be able to show the vision and identify the sections of the website.

INSPIRATION:
We typically add a couple of links in the brief of websites we like to help you get started in your design.

REVISIONS:
We do not often ask for revisions of the designs unless we see something in the design that may not appeal to the client. If there are slight changes that we want to make, we do that in the development process.

FEEDBACK:
We rarely give feedback on designs during the design process. We are working on many website projects and do not have the time to provide feedback. We usually respond if your request is well thought out and asks specific questions, but a note asking “feedback, please” usually goes unanswered.

```html
<!DOCTYPE html>
<html lang="en">
<head>
<meta charset="utf-8">
<title>Brennock Group — Law Enforcement Consulting</title>
<link rel="stylesheet" href="https://fonts.googleapis.com/css2?family=Outfit:wght@500;600;700&family=Poppins:wght@400;500;600&display=swap">
<style>
:root{
  --orange:#e54b1e;
  --ink:#111111;
  --black:#000000;
  --footer:#1b1b1b;
  --paper:#ffffff;
  --mist:#eeeff0;
  --grey:#555555;
  --line:#cfcfcf;
}
*{margin:0;padding:0;box-sizing:border-box}
html,body{width:1200px;height:5329px;overflow:hidden;background:var(--paper)}
body{position:relative;font-family:"Poppins",sans-serif;color:var(--ink)}
.abs{position:absolute}
h1,h2,h3{font-family:"Outfit",sans-serif;font-weight:600;line-height:1.12}
.accent{color:var(--orange)}
p{font-size:14.5px;line-height:1.62;color:var(--grey)}
.photo{position:absolute}

/* brand */
.brand{display:flex;align-items:center;gap:12px}
.brand-mark{width:44px;height:44px;border-radius:50%;background:var(--orange);flex:none}
.brand-name{font-family:"Poppins",sans-serif;font-weight:600;font-size:22px;color:var(--orange);white-space:nowrap}

/* nav */
.nav{left:355px;top:50px;display:flex;gap:36px;font-size:13px;font-weight:500}
.nav a{color:var(--ink);text-decoration:none;position:relative}
.nav a.active::after{content:"";position:absolute;left:0;right:0;bottom:-12px;height:3px;background:var(--orange)}

/* button */
.btn{position:absolute;width:286px;height:42px;display:flex;align-items:center;justify-content:center}
.btn::before{content:"";position:absolute;left:28px;right:28px;top:0;bottom:0;background:var(--orange);clip-path:polygon(0 0,100% 0,calc(100% - 22px) 100%,22px 100%)}
.btn i{position:absolute;top:0;width:36px;height:42px;background:var(--orange)}
.btn i.l{left:0;clip-path:polygon(0 0,14px 0,36px 100%,22px 100%)}
.btn i.r{right:0;clip-path:polygon(22px 0,36px 0,14px 100%,0 100%)}
.btn span{position:relative;color:#fff;font-size:13px;font-weight:600;letter-spacing:.3px}

/* hero */
.hero{left:0;top:0;width:1200px;height:689px;background:linear-gradient(180deg,#f4f4f4,#ececec);overflow:hidden}
.hero-title{left:100px;top:238px;width:480px;text-align:center;font-size:52px}
.hero-copy{left:130px;top:378px;width:420px;text-align:center;color:var(--ink);font-size:15px;line-height:1.4}

/* about */
.about-title{left:126px;top:858px;font-size:40px}
.about-copy{left:126px;top:925px;width:460px;font-size:13.5px}

/* trusted */
.trusted-band{left:0;top:1572px;width:1200px;height:654px;background:var(--black);overflow:hidden}
.trusted-title{left:685px;top:1652px;font-size:42px;color:#fff}
.trusted-copy{left:685px;top:1824px;width:405px;color:#fff;font-size:13.5px}

/* training */
.training-title{left:0;top:2325px;width:1200px;text-align:center;font-size:40px}
.training-sub{left:0;top:2444px;width:1200px;text-align:center;font-size:16px;font-weight:600}
.service{position:absolute;top:2524px;width:280px;text-align:center}
.service svg{display:block;margin:0 auto}
.service h3{font-size:21px;margin-top:36px}
.service p{margin-top:22px;font-size:13.5px;line-height:1.35;color:var(--ink)}

/* protection */
.protect{left:0;top:3031px;width:1200px;height:590px;background:var(--mist);overflow:hidden}
.protect-title{left:126px;top:3190px;font-size:42px}
.protect-copy{left:126px;top:3260px;width:460px;font-size:13.5px}

/* faq */
.faq-title{left:0;top:3730px;width:1200px;text-align:center;font-size:42px}
.faq-item{position:absolute;width:422px;height:80px;border-bottom:1.5px solid var(--line);display:flex;align-items:center;justify-content:space-between;padding:0 6px;font-size:17px;font-weight:600}
.faq-item b{font-size:20px;font-weight:600}

/* cta */
.cta{left:0;top:4279px;width:1200px;height:583px;background:#f1f1f1;overflow:hidden}
.cta-title{left:126px;top:4405px;font-size:42px}
.cta-copy{left:126px;top:4535px;width:380px;font-size:13.5px}

/* footer */
.footer{left:0;top:4862px;width:1200px;height:467px;background:var(--footer)}
.foot-copy{left:126px;top:5065px;width:360px;color:#fff;font-size:14px}
.foot-col{position:absolute;top:4948px}
.foot-col h3{color:#fff;font-size:26px;font-weight:500;margin-bottom:28px}
.foot-col a{display:block;color:#fff;text-decoration:none;font-size:13.5px;margin-bottom:17px}
.foot-rule{left:126px;top:5244px;width:948px;height:1px;background:#5a5a5a}
.social{left:126px;top:5278px;display:flex;gap:10px}
.social span{width:16px;height:16px;border:1.6px solid #fff;border-radius:3px}
.copyright{left:765px;top:5278px;color:#fff;font-size:13.5px}
</style>
</head>
<body>

<!-- Hero -->
<section class="hero abs">
  <svg class="abs" style="left:0;top:0" width="1200" height="689" viewBox="0 0 1200 689">
    <polygon points="930,0 1200,0 1200,390 1010,689 760,689" fill="#e54b1e"/>
    <path d="M0 600 C60 560 150 540 200 570 L300 689" fill="none" stroke="#f0cfc3" stroke-width="26"/>
  </svg>
  <div class="photo" role="img" aria-label="Smiling consultant in a navy suit with arms crossed" style="left:625px;top:120px;width:430px;height:569px;background:linear-gradient(180deg,#6f6f73 0%,#2c3a5a 40%,#1f2c47 100%);border-radius:190px 190px 0 0"></div>
</section>

<div class="brand abs" style="left:64px;top:36px">
  <span class="brand-mark"></span><span class="brand-name">Brennock Group</span>
</div>

<nav class="nav abs">
  <a class="active">HOME</a><a>SERVICES</a><a>STAFF</a><a>ABOUT US</a><a>CLIENTS</a><a>CONTACT</a>
</nav>

<h1 class="hero-title abs">Law Enforcement Consulting Group</h1>
<p class="hero-copy abs">Lorem ipsum dolor sloreit amet, consecteturad piscing elit, sed do eiusmod tempor.</p>
<a class="btn" style="left:195px;top:452px"><i class="l"></i><i class="r"></i><span>GET STARTED HERE</span></a>

<!-- About -->
<h2 class="about-title abs"><span class="accent">About</span> Brennock Group</h2>
<p class="about-copy abs">Lorem ipsum dolor sit amet, consectetur adip isci ng elit, sed do eiusmod tempor incididunt ut labore et dolore mag na aliqua. Quis ipsum suspen dis se ultri ces gravida. Risus commodo viverra maec enas acc umsan lacus vel facilisis. Lorem ipsum dolor sit amet, consectetur adip isci ng elitse do eiusmod tempor incididunt ut labo re et dolore magna aliqua. Quis ipsum suspen dis se ultric.maec enas acc um san lacus vel facilisis. Lorem ipsum dolor sit amet, consect etur adip isci ng elit, sed do eiusmod te.</p>
<div class="abs" style="left:680px;top:880px;width:380px;height:380px;border-radius:50%;background:#fff;box-shadow:0 6px 24px rgba(0,0,0,.12);display:flex;align-items:center;justify-content:center">
  <span class="brand-name" style="font-size:34px">Brennock Group</span>
</div>

<!-- Trusted resource -->
<section class="trusted-band abs">
  <svg class="abs" style="left:0;top:0" width="1200" height="654" viewBox="0 0 1200 654">
    <path d="M1040 654 L1040 560 Q1040 520 1080 495 L1200 420 L1200 470 L1100 535 Q1080 548 1080 575 L1080 654 Z" fill="#e54b1e"/>
  </svg>
</section>

<!-- hexagon frame: orange strips behind, white frame, photo on top -->
<svg class="abs" style="left:40px;top:1420px" width="620" height="630" viewBox="0 0 620 630">
  <!-- top-right orange strip -->
  <polygon points="440,20 592,106 592,420 566,420 566,122 428,44" fill="#e54b1e"/>
  <!-- left orange strip -->
  <polygon points="26,170 52,170 52,440 100,468 86,490 26,456" fill="#e54b1e"/>
  <!-- white hexagon frame -->
  <polygon points="310,-40 585,118 585,460 310,620 35,460 35,118" fill="#fff"/>
</svg>
<div class="photo" role="img" aria-label="Confident consultant in a navy suit with arms crossed, office backdrop" style="left:95px;top:1345px;width:510px;height:675px;background:linear-gradient(180deg,#8c8f93 0%,#36456a 45%,#1e2a45 100%);clip-path:polygon(36% 0,64% 0,64% 10%,100% 27%,100% 77%,50% 100%,0 77%,0 27%,36% 10%)"></div>

<h2 class="trusted-title abs">A Trusted<br>Resource for <span class="accent">Law<br>Enforcement</span></h2>
<p class="trusted-copy abs">Lorem ipsum dolor sit amet, consectetur adip isci ng elit, sed do eiusmod tempor incididunt ut labo re et dolore magna aliqua. Quis ipsum suspen dis se ultri ces gravida. Risus commodo viverra maec enas acc umsan lacus vel facilisis. Lorem ipsum dolor sit amet, consectetur adip isci ng elit, sed do eiusmod tempor incididunt ut labo re et dolore magna aliqua. Quis ipsum suspen dis se ultrices gravida. Risus comm odo viverra maec enas acccilisis.</p>

<!-- Training -->
<h2 class="training-title abs"><span class="accent">Law Enforcement</span><br>Training Opportunities</h2>
<div class="training-sub abs">Services we offer:</div>

<div class="service" style="left:115px">
  <svg width="170" height="176" viewBox="0 0 170 176">
    <path d="M70 8 L20 36 Q8 43 8 56 L8 110" fill="none" stroke="#e54b1e" stroke-width="12"/>
    <path d="M100 8 L150 36 Q162 43 162 56 L162 110" fill="none" stroke="#e54b1e" stroke-width="12"/>
    <path d="M20 135 L85 170 L150 135" fill="none" stroke="#e54b1e" stroke-width="12"/>
    <g fill="none" stroke="#111" stroke-width="3">
      <circle cx="62" cy="68" r="8"/><circle cx="108" cy="68" r="8"/><circle cx="85" cy="80" r="9"/>
      <path d="M48 100 Q62 80 76 94"/><path d="M94 94 Q108 80 122 100"/><path d="M66 118 Q85 92 104 118"/>
      <line x1="55" y1="120" x2="115" y2="120"/>
    </g>
  </svg>
  <h3>On-site Training<br>Services</h3>
  <p>Lorem ipsum dolor sit amet, consectetur adipiscing elit, sed do eiusmod tempor incididunt ut labore et dolore magna lor.</p>
</div>
<div class="service" style="left:460px">
  <svg width="170" height="176" viewBox="0 0 170 176">
    <path d="M70 8 L20 36 Q8 43 8 56 L8 110" fill="none" stroke="#e54b1e" stroke-width="12"/>
    <path d="M100 8 L150 36 Q162 43 162 56 L162 110" fill="none" stroke="#e54b1e" stroke-width="12"/>
    <path d="M20 135 L85 170 L150 135" fill="none" stroke="#e54b1e" stroke-width="12"/>
    <g fill="none" stroke="#111" stroke-width="3">
      <circle cx="85" cy="70" r="18" stroke-dasharray="6 4"/><circle cx="85" cy="70" r="8"/>
      <circle cx="62" cy="98" r="6"/><circle cx="85" cy="98" r="6"/><circle cx="108" cy="98" r="6"/>
      <path d="M52 120 Q62 106 72 120 M75 120 Q85 106 95 120 M98 120 Q108 106 118 120"/>
    </g>
  </svg>
  <h3>Management<br>Structures</h3>
  <p>Lorem ipsum dolor sit amet, consectetur adipiscing elit, sed do eiusmod tempor incididunt ut labore et dolore magna lor.</p>
</div>
<div class="service" style="left:804px">
  <svg width="170" height="176" viewBox="0 0 170 176">
    <path d="M70 8 L20 36 Q8 43 8 56 L8 110" fill="none" stroke="#e54b1e" stroke-width="12"/>
    <path d="M100 8 L150 36 Q162 43 162 56 L162 110" fill="none" stroke="#e54b1e" stroke-width="12"/>
    <path d="M20 135 L85 170 L150 135" fill="none" stroke="#e54b1e" stroke-width="12"/>
    <g fill="none" stroke="#111" stroke-width="3">
      <path d="M60 60 L85 52 L110 60 L110 88 Q110 108 85 120 Q60 108 60 88 Z"/>
      <path d="M80 94 L96 80 Q104 76 112 84 L122 94 L108 104 Z"/>
    </g>
  </svg>
  <h3>Development<br>Impacts</h3>
  <p>Lorem ipsum dolor sit amet, consectetur adipiscing elit, sed do eiusmod tempor incididunt ut labore et dolore magna lor.</p>
</div>

<!-- Protection -->
<section class="protect abs">
  <div class="abs" style="left:870px;top:90px;width:330px;height:500px;background:var(--orange);border-radius:60px 0 0 0"></div>
  <div class="photo" role="img" aria-label="Consultant in a navy suit holding a tablet" style="left:650px;top:25px;width:470px;height:565px;background:linear-gradient(180deg,#8a8d92 0%,#2f3c5c 40%,#1e2944 100%);border-radius:200px 200px 0 0"></div>
</section>
<h2 class="protect-title abs"><span class="accent">Protection</span> Starts Here</h2>
<p class="protect-copy abs">Lorem ipsum dolor sit amet, consectetur adip isci ng elit, sed do eiusmod tempor incididunt ut labore et dolore mag na aliqua. Quis ipsum suspen dis se ultri ces gravida. Risus commodo viverra maec enas acc umsan lacus vel facilisis. Lorem ipsum dolor sit amet, consectetur adip isci ng elit, sed do eiusmod tempor incididunt ut labore et dolore magna aliqua. Quis ipsum suspen dis se ultric.</p>
<a class="btn" style="left:128px;top:3436px"><i class="l"></i><i class="r"></i><span>GET STARTED HERE</span></a>

<!-- FAQ -->
<h2 class="faq-title abs"><span class="accent">Frequently</span> Asked Questions</h2>
<div class="faq-item" style="left:128px;top:3812px">Lorem ipsusit amet onsectetur ?<b>+</b></div>
<div class="faq-item" style="left:128px;top:3892px">Lorem ipsusit amet onsectetur ?<b>+</b></div>
<div class="faq-item" style="left:128px;top:3972px">Lorem ipsusit amet onsectetur ?<b>+</b></div>
<div class="faq-item" style="left:128px;top:4052px">Lorem ipsusit amet onsectetur ?<b>+</b></div>
<div class="faq-item" style="left:652px;top:3812px">Lorem ipsusit amet onsectetur ?<b>+</b></div>
<div class="faq-item" style="left:652px;top:3892px">Lorem ipsusit amet onsectetur ?<b>+</b></div>
<div class="faq-item" style="left:652px;top:3972px">Lorem ipsusit amet onsectetur ?<b>+</b></div>
<div class="faq-item" style="left:652px;top:4052px">Lorem ipsusit amet onsectetur ?<b>+</b></div>

<!-- Call to action -->
<section class="cta abs">
  <div class="photo" role="img" aria-label="Consultant with glasses working on a laptop in a bright office" style="left:560px;top:0;width:640px;height:583px;background:linear-gradient(90deg,#f1f1f1 0%,#d9dadc 25%,#b9bbbe 60%,#8e9196 100%)"></div>
</section>
<h2 class="cta-title abs"><span class="accent">Start your protection</span><br>training now</h2>
<p class="cta-copy abs">Lorem ipsum dolor sit amet, consectetur adip isci ng elitsed do eiusmod tempor incididunt ut labo re et dolore magna aliqua. Quis ipsum suspen dis se ultri ces gravida. Risus commodo viverra maec enas acc umsan lacus vel facilisis. Lorem ipsum dolor sit amet, consectetur adip.</p>
<a class="btn" style="left:126px;top:4701px"><i class="l"></i><i class="r"></i><span>GET STARTED HERE</span></a>

<!-- Footer -->
<footer class="footer abs"></footer>
<div class="brand abs" style="left:126px;top:4962px">
  <span class="brand-mark"></span><span class="brand-name">Brennock Group</span>
</div>
<p class="foot-copy abs">Lorem ipsum dolor sit amet, consectetur adipiscing elit, sed do eiusmod tempor incidi dunt ut labore et dolore magna aliqua. Quis ipsum suspendisse ultrices gravida.</p>
<div class="foot-col" style="left:635px">
  <h3>About Us</h3>
  <a>Services</a><a>Our Story</a><a>Newsroom</a><a>Careers</a><a>Testimonials</a><a>Contact</a>
</div>
<div class="foot-col" style="left:842px">
  <h3>Services</h3>
  <a>On-site training</a><a>Community Development</a><a>Parks, Recreation, &amp; Library</a><a>Economic Development</a><a>Human Resources</a><a>Administrative Services</a>
</div>
<div class="foot-rule abs"></div>
<div class="social abs"><span></span><span></span><span></span></div>
<div class="copyright abs">Copyright © 2025 All Rights Are Reserved.</div>

</body>
</html>
```